Brake Caliper Box Design - 4 Sizes

We need new packaging design for our products. We are a company based in Montreal, Quebec and we re-manufacture calipers. This project requires that 4 box sizes be designed (same overall design). The boxes need to be bilingual (French and English). Our products are top quality premium products and the boxes should reflect that, we want something modern, very professional and it needs to be much more refined and polished than our previous design. 3D renders would be much appreciated.

The text in the previous design is to be re-used, also the new design should incorporate two badges (Gaurantee and Certified badge)

I have included our previous design for reference only. This design MUST be completely different. You will need to design a logo for this box.

We need the designs delivered in .eps and .jpg format.

******** Update ************

We still think some people have misunderstood what brand they are designing boxes for. We need boxes designed for a new brand called "ZOR Meridian". Along with the boxes we need a logo for this new brand. The logo and box design CANNOT LOOK, FEEL and BE anything like the sample box designs we provided. These sample box designs were supplied only for size and to provide text/images for the new design (besides the LOGO).

Target Market(s)

Auto Part Stores

Logo Text

ZOR MERIDIAN

Requirements
Must have
• caliper pictures, 2 year Gaurantee badge and Certified badge

```html
<!DOCTYPE html>
<html lang="fr">
<head>
<meta charset="utf-8">
<title>ZOR Meridian – Étriers de freins à disques</title>
<link rel="stylesheet" href="https://fonts.googleapis.com/css2?family=Montserrat:wght@400;600;700;800&display=swap">
<style>
  :root{
    --bg:#f1f1f3;
    --silver-light:#ffffff;
    --silver-mid:#d9d9dc;
    --silver-deep:#a9a9ad;
    --charcoal:#2b2b2d;
    --ink:#1d1d1f;
    --brand-red:#c0182e;
    --badge-grey:#6e6e72;
    --photo-a:#9b9a97;
    --photo-b:#cfcdc8;
  }
  *{box-sizing:border-box;margin:0;padding:0}
  html,body{width:1200px;height:1200px;overflow:hidden}
  body{background:var(--bg);font-family:"Montserrat",Arial,sans-serif;color:var(--ink)}
  .sheet{position:relative;width:1200px;height:1200px;
    display:grid;grid-template-columns:720px 400px;grid-template-rows:440px 440px;
    gap:24px;padding:148px 28px}
  .panel{position:relative;overflow:hidden;
    background:linear-gradient(135deg,var(--silver-light) 0%,var(--silver-mid) 45%,var(--silver-light) 60%,var(--silver-deep) 100%);
    box-shadow:0 6px 18px rgba(0,0,0,.12)}
  .panel::before,.panel::after{content:"";position:absolute;top:0;bottom:0;width:70px;
    background:linear-gradient(90deg,#3a3a3d,#8c8c90)}
  .panel::before{left:0}
  .panel::after{right:0;transform:scaleX(-1)}
  .band{position:absolute;left:0;right:0;bottom:0;height:54px;background:var(--charcoal);
    color:#fff;font-size:9.5px;font-weight:600;display:flex;align-items:center;
    justify-content:space-between;padding:0 78px;z-index:2}
  .band span{white-space:nowrap}
  .brand{position:absolute;display:flex;align-items:center;gap:10px;z-index:2;white-space:nowrap}
  .brand-dot{width:20px;height:20px;border-radius:50%;background:var(--brand-red);flex:none}
  .brand-name{font-weight:800;color:var(--brand-red);letter-spacing:1px;line-height:1}
  .ribbons{position:absolute;display:flex;flex-direction:column;gap:5px;z-index:2;width:204px}
  .ribbon{background:var(--brand-red);color:#fff;font-weight:700;font-size:13px;
    padding:5px 10px;text-align:center;white-space:nowrap}
  .photo{position:absolute;border-radius:14px;
    background:radial-gradient(circle at 40% 40%,var(--photo-b),var(--photo-a));z-index:1}
  .badge-guarantee,.badge-certified{position:absolute;z-index:2}
  .badge-certified{width:42px;height:42px;border-radius:50%;background:var(--charcoal);
    border:3px solid var(--silver-mid)}
  .fine{position:absolute;font-size:9px;font-weight:600;line-height:1.4;z-index:2;white-space:nowrap}
  .choice{position:absolute;width:130px;height:130px;border-radius:50%;background:var(--badge-grey);
    color:#fff;font-size:11px;font-weight:700;text-align:center;display:flex;
    flex-direction:column;justify-content:center;line-height:1.35;z-index:2}
  .conditions-title{position:absolute;left:80px;right:80px;top:196px;text-align:center;
    font-size:18px;letter-spacing:6px;font-weight:600;z-index:2}
  .conditions-rule{position:absolute;left:100px;right:100px;top:226px;height:2px;background:var(--ink)}
  .conditions-text{position:absolute;left:84px;right:84px;top:242px;text-align:center;
    font-size:10px;font-weight:600;line-height:1.5;z-index:2}
  .important{position:absolute;left:88px;top:240px;width:226px;font-size:10px;line-height:1.5;z-index:2}
  .important strong{font-weight:800}
</style>
</head>
<body>
<main class="sheet">

  <!-- Front panel -->
  <section class="panel panel-front">
    <div class="brand" style="left:100px;top:62px">
      <span class="brand-dot"></span><span class="brand-name" style="font-size:36px">ZOR MERIDIAN</span>
    </div>
    <div class="ribbons" style="right:90px;top:120px">
      <span class="ribbon">Étriers de freins à disques</span>
      <span class="ribbon">Disc Brake Caliper</span>
    </div>
    <p class="fine" style="left:90px;top:180px">QUALITÉ GARANTIE / ÉPROUVÉ À 100%<br>100% PRETESTED FOR GARANTEED QUALITY</p>
    <div class="photo" role="img" aria-label="Étrier de frein remanufacturé" style="left:262px;top:230px;width:116px;height:116px"></div>
    <div class="photo" role="img" aria-label="Étrier de frein remanufacturé" style="left:396px;top:222px;width:116px;height:116px"></div>
    <div class="photo" role="img" aria-label="Étrier de frein remanufacturé" style="left:530px;top:214px;width:110px;height:116px"></div>
    <svg class="badge-guarantee" style="left:100px;top:240px" width="40" height="46" viewBox="0 0 40 46" aria-label="Garantie 2 ans"><path d="M20 2 L38 9 V24 C38 35 29 42 20 45 C11 42 2 35 2 24 V9 Z" fill="var(--charcoal)" stroke="var(--silver-mid)" stroke-width="3"/></svg>
    <span class="badge-certified" aria-label="Certifié" style="left:155px;top:242px"></span>
    <div class="band"><span>Voir les conditions de remboursements sous la boîte</span><span>For returning conditions, look under the box</span></div>
  </section>

  <!-- Side panel -->
  <section class="panel panel-side">
    <div class="brand" style="left:88px;top:72px">
      <span class="brand-dot"></span><span class="brand-name" style="font-size:22px">ZOR MERIDIAN</span>
    </div>
    <div class="ribbons" style="left:88px;top:120px">
      <span class="ribbon">Étriers de freins à disques</span>
      <span class="ribbon">Disc Brake Caliper</span>
    </div>
    <p class="important"><strong>IMPORTANT :</strong><br>Les instructions contenues dans la boîte doivent être lues attentivement.<br><strong>IMPORTANT :</strong><br>Read critical information enclosed.</p>
    <div class="band" style="justify-content:center;gap:10px;font-size:10px;padding:0 72px">
      <svg width="14" height="16" viewBox="0 0 14 16" aria-hidden="true"><path d="M7 1 L13 8 H9 V15 H5 V8 H1 Z" fill="#fff"/></svg>
      <span>CE CÔTÉ EN HAUT / THIS SIDE UP</span>
    </div>
  </section>

  <!-- Lid panel -->
  <section class="panel panel-lid">
    <div class="brand" style="left:100px;top:62px">
      <span class="brand-dot"></span><span class="brand-name" style="font-size:36px">ZOR MERIDIAN</span>
    </div>
    <div class="ribbons" style="left:100px;top:120px">
      <span class="ribbon">Étriers de freins à disques</span>
      <span class="ribbon">Disc Brake Caliper</span>
    </div>
    <div class="choice" style="right:100px;top:50px"><span>LE CHOIX DES</span><span>PROFESSIONNELS</span><span>PROFESSIONAL'S</span><span>CHOICE</span></div>
    <div class="photo" role="img" aria-label="Étrier de frein remanufacturé" style="left:130px;top:240px;width:110px;height:110px"></div>
    <div class="photo" role="img" aria-label="Étrier de frein remanufacturé" style="left:255px;top:230px;width:110px;height:110px"></div>
    <div class="photo" role="img" aria-label="Étrier de frein remanufacturé" style="left:380px;top:220px;width:110px;height:110px"></div>
    <span class="badge-certified" aria-label="Certifié" style="left:512px;top:252px"></span>
    <svg class="badge-guarantee" style="left:570px;top:250px" width="40" height="46" viewBox="0 0 40 46" aria-label="Garantie 2 ans"><path d="M20 2 L38 9 V24 C38 35 29 42 20 45 C11 42 2 35 2 24 V9 Z" fill="var(--charcoal)" stroke="var(--silver-mid)" stroke-width="3"/></svg>
  </section>

  <!-- Bottom panel -->
  <section class="panel panel-bottom">
    <div class="brand" style="left:88px;top:54px">
      <span class="brand-dot"></span><span class="brand-name" style="font-size:22px">ZOR MERIDIAN</span>
    </div>
    <div class="ribbons" style="left:88px;top:100px">
      <span class="ribbon">Étriers de freins à disques</span>
      <span class="ribbon">Disc Brake Caliper</span>
    </div>
    <h2 class="conditions-title">CONDITIONS</h2>
    <span class="conditions-rule"></span>
    <p class="conditions-text">Afin de recevoir votre crédit dans sa totalité, l'unité doit être retournée entière et dans sa boîte originale.<br>To receive full credit, the complete unit must be returned into it's original box.</p>
  </section>

</main>
</body>
</html>
```